Quorvex Labworks Website

All the descriptions are available in the attached file. The designer has to structure the website and find the right images and icons. The website should look modern and avoid using images of real humans rather use animated images. Please note that the design should include home page, all the 4 services page , the contact us would be at the bottom of home page.

```html
<!DOCTYPE html>
<html lang="en">
<head>
<meta charset="utf-8">
<title>Quorvex Labworks</title>
<link href="https://fonts.googleapis.com/css2?family=Poppins:wght@400;500;600&display=swap" rel="stylesheet">
<style>
:root{
  --blue:#2f6fba;
  --blue-dark:#2a64a9;
  --orange:#f7941d;
  --green:#52b03f;
  --ink:#222;
  --muted:#555;
  --grey:#ececec;
  --field:#ffffff;
}
*{box-sizing:border-box;margin:0;padding:0}
html,body{width:1200px;height:3713px;overflow:hidden}
body{font-family:'Poppins',sans-serif;color:var(--ink);background:#fff;position:relative}
.abs{position:absolute}
a{color:inherit;text-decoration:none}

/* header */
.site-header{left:0;top:0;width:1200px;height:101px;background:#fff}
.brand{left:85px;top:30px;font-size:24px;font-weight:600;color:var(--blue);line-height:1.1;display:flex;align-items:center;gap:10px}
.brand .dot{width:14px;height:14px;background:var(--orange);display:inline-block}
.main-nav{right:87px;top:48px;display:flex;gap:38px;font-size:15px;color:#333}
.main-nav .caret{color:var(--blue);font-size:10px;margin-left:4px}

/* hero */
.hero{left:0;top:101px;width:1200px;height:500px;background:linear-gradient(90deg,#ececec 0%,#e4e4e4 45%,#d9d6d2 100%)}
.hero-photo{left:560px;top:0;width:640px;height:500px;background:linear-gradient(100deg,rgba(230,230,230,0) 0%,#cfc8c0 35%,#9d9288 75%,#6f655c 100%)}
.hero h1{left:105px;top:101px;font-size:42px;font-weight:500;line-height:1.22;color:#1d1d1d;letter-spacing:.3px}
.hero p{left:107px;top:213px;width:520px;font-size:21px;line-height:1.25;color:#333}
.btn-blue{background:var(--blue);color:#fff;display:flex;align-items:center;justify-content:center;font-weight:500}
.hero .btn-blue{left:107px;top:300px;width:194px;height:49px;font-size:19px}
.dots{left:113px;top:413px;display:flex;gap:7px}
.dots span{width:9px;height:9px;background:#fff}
.dots span:first-child{background:var(--blue)}

/* section heading */
.sec-title{font-size:40px;font-weight:600;color:var(--blue);letter-spacing:.5px;display:flex;align-items:flex-end;gap:12px}
.mark{position:relative;width:62px;height:72px;flex:none}
.mark i{position:absolute;width:22px;height:22px}
.mark .g{left:17px;top:0;background:var(--green)}
.mark .o{left:40px;top:20px;width:28px;height:28px;background:var(--orange)}
.mark .b{left:0;top:47px;width:26px;height:26px;background:var(--blue)}

/* services */
.services{left:0;top:601px;width:1200px;height:912px;background:#fff}
.services .sec-title{left:455px;top:70px}
.svc{width:330px}
.svc h3{font-size:25px;font-weight:600;color:var(--blue);margin-bottom:4px}
.svc p{font-size:15.5px;line-height:1.65;color:#333}
.svc .btn{display:inline-flex;align-items:center;justify-content:center;width:156px;height:32px;color:#fff;font-size:15px;margin-top:10px}
.svc.right{text-align:right}
.svc.right .btn{margin-right:2px}
.btn.orange{background:var(--orange)}
.btn.green{background:var(--green)}
.hub{left:380px;top:258px}

/* about */
.about{left:0;top:1513px;width:1200px;height:515px;background:var(--grey)}
.about-photo{left:620px;top:0;width:580px;height:515px;background:linear-gradient(90deg,rgba(236,236,236,0) 0%,#e3e1de 25%,#c9d4e2 55%,#9fb4cd 80%,#d6d4d0 100%)}
.about .sec-title{left:124px;top:70px}
.about h4{left:120px;top:212px;font-size:21px;font-weight:500;color:#222}
.about p{left:122px;top:245px;width:500px;font-size:16px;line-height:1.6;color:#333}
.about .btn-blue{left:122px;top:387px;width:206px;height:58px;font-size:18px}

/* blog */
.blog{left:0;top:2028px;width:1200px;height:720px;background:#fff}
.blog .sec-title{left:473px;top:38px}
.card{top:208px;width:309px;height:453px;background:#fff;box-shadow:0 1px 5px rgba(0,0,0,.25)}
.card .thumb{width:309px;height:225px;background:linear-gradient(180deg,#c8ccce 0%,#8f9597 45%,#4d4a45 100%)}
.card .date{margin:22px 0 0 19px;font-size:13px;color:#666}
.card h5{margin:14px 0 0 19px;font-size:17px;font-weight:600;color:#222}
.card p{margin:4px 19px 0;font-size:14px;line-height:1.3;color:#333}
.card .btn-blue{margin:20px 0 0 19px;width:96px;height:31px;font-size:13px}

/* contact */
.contact{left:0;top:2748px;width:1200px;height:545px;background:var(--grey)}
.contact .sec-title{left:473px;top:60px}
.field{background:var(--field);font-size:17px;color:#666;padding:0 27px;display:flex;align-items:center}
.field.msg{align-items:flex-start;padding-top:22px;padding-left:19px}
.contact .btn-blue{left:640px;top:399px;width:222px;height:61px;font-size:18px}

/* info bar */
.info{left:0;top:3293px;width:1200px;height:158px;background:#fff}
.info-item{top:47px;display:flex;align-items:center;gap:20px;font-size:15.5px;color:#333;line-height:1.3}
.info-item .ic{width:55px;height:55px;display:flex;align-items:center;justify-content:center;flex:none}

/* footer */
.footer{left:0;top:3451px;width:1200px;height:262px;background:var(--blue)}
.footer .brand{left:80px;top:70px;color:#fff;font-size:30px}
.footer .brand .dot{background:#fff}
.foot-nav{right:90px;top:96px;display:flex;font-size:18px;color:#fff}
.foot-nav a{padding:0 20px;border-left:2px solid #fff;line-height:26px}
.foot-nav a:first-child{border-left:none}
.rule{left:85px;top:169px;width:1028px;height:1px;background:rgba(255,255,255,.45)}
.copy{left:85px;top:209px;font-size:12px;color:#fff}
.social{left:944px;top:204px;display:flex;gap:20px}
.social span{width:26px;height:26px;border:1.5px solid #fff;border-radius:50%}
</style>
</head>
<body>

<header class="site-header abs">
  <div class="brand abs"><span class="dot"></span>Quorvex Labworks</div>
  <nav class="main-nav abs">
    <a href="#">Home</a>
    <a href="#">Services<span class="caret">▼</span></a>
    <a href="#">Products</a>
    <a href="#">Blog</a>
    <a href="#">Contact Us</a>
  </nav>
</header>

<section class="hero abs">
  <div class="hero-photo abs" role="img" aria-label="Two consultants reviewing documents at a desk"></div>
  <h1 class="abs">ADVANCING INNOVATION<br>THROUGH IT CONSULTING</h1>
  <p class="abs">Empower your digital journey with our advanced IT solutions. From data to web and mobile apps,</p>
  <a class="btn-blue abs" href="#">Know More</a>
  <div class="dots abs"><span></span><span></span><span></span><span></span></div>
</section>

<section class="services abs">
  <h2 class="sec-title abs">OUR SERVICES<span class="mark"><i class="g"></i><i class="o"></i><i class="b"></i></span></h2>

  <div class="svc right abs" style="left:40px;top:265px">
    <h3>Data Analytics</h3>
    <p>Lorem ipsum dolor sit amet, consec<br>tetur adipiscing elit Lorem ipsum dolor</p>
    <a class="btn orange" href="#">Read More</a>
  </div>
  <div class="svc abs" style="left:837px;top:265px">
    <h3>Web Development</h3>
    <p>Lorem ipsum dolor sit amet, consec<br>tetur adipiscing elit Lorem ipsum dolor</p>
    <a class="btn green" href="#">Read More</a>
  </div>
  <div class="svc right abs" style="left:47px;top:600px">
    <h3>Start-up Partner</h3>
    <p>Lorem ipsum dolor sit amet, consec<br>tetur adipiscing elit Lorem ipsum dolor</p>
    <a class="btn green" href="#">Read More</a>
  </div>
  <div class="svc abs" style="left:829px;top:600px">
    <h3>Mobile App&nbsp; Development</h3>
    <p>Lorem ipsum dolor sit amet, consec<br>tetur adipiscing elit Lorem ipsum dolor</p>
    <a class="btn orange" href="#">Read More</a>
  </div>

  <svg class="hub abs" width="450" height="480" viewBox="380 859 450 480" aria-label="Service overview">
    <circle cx="605" cy="1084" r="222" fill="none" stroke="var(--blue)" stroke-width="4"/>
    <circle cx="605" cy="1084" r="182" fill="var(--blue)"/>
    <text x="605" y="1078" text-anchor="middle" font-family="Poppins,sans-serif" font-size="32" font-weight="600" fill="#fff">Quorvex</text>
    <text x="605" y="1118" text-anchor="middle" font-family="Poppins,sans-serif" font-size="32" font-weight="600" fill="#fff">Labworks</text>
    <g fill="#fff" stroke="var(--blue)" stroke-width="5">
      <circle cx="471" cy="944" r="76"/>
      <circle cx="725" cy="940" r="76"/>
      <circle cx="483" cy="1251" r="76"/>
      <circle cx="710" cy="1251" r="76"/>
    </g>
    <!-- analytics -->
    <g fill="none" stroke="var(--blue)" stroke-width="3">
      <path d="M440 970 V925 M450 970 V935 M460 970 V915 M440 970 H475"/>
      <circle cx="481" cy="950" r="14"/>
      <path d="M491 960 L503 972"/>
    </g>
    <!-- web -->
    <g fill="var(--blue)">
      <circle cx="704" cy="918" r="8"/>
      <path d="M692 950 q12 -20 24 0 v12 h-24z"/>
      <rect x="714" y="924" width="40" height="28" rx="2" fill="none" stroke="var(--blue)" stroke-width="3"/>
      <rect x="720" y="954" width="34" height="6"/>
    </g>
    <!-- rocket -->
    <g fill="var(--blue)">
      <path d="M483 1213 q16 18 16 44 v14 h-32 v-14 q0 -26 16 -44z"/>
      <path d="M467 1254 l-10 20 h10z M499 1254 l10 20 h-10z"/>
      <circle cx="483" cy="1245" r="5" fill="#fff"/>
    </g>
    <!-- mobile -->
    <g fill="none" stroke="var(--blue)" stroke-width="3">
      <rect x="695" y="1224" width="30" height="52" rx="4"/>
      <circle cx="710" cy="1250" r="6"/>
      <path d="M703 1268 h14"/>
    </g>
  </svg>
</section>

<section class="about abs">
  <div class="about-photo abs" role="img" aria-label="Professional holding a laptop in a planning office"></div>
  <h2 class="sec-title abs">ABOUT QUORVEX LABWORKS<span class="mark"><i class="g"></i><i class="o"></i><i class="b"></i></span></h2>
  <h4 class="abs">Advancing Innovation Through IT Consulting</h4>
  <p class="abs">We are a forward-thinking IT consulting firm specializing in providing cutting-edge data analytics, web application development, and mobile app development services. Our passion for innovation and technology drives us to deliver tailor-made solu-</p>
  <a class="btn-blue abs" href="#">Know More</a>
</section>

<section class="blog abs">
  <h2 class="sec-title abs">LATEST BLOG<span class="mark"><i class="g"></i><i class="o"></i><i class="b"></i></span></h2>
  <article class="card abs" style="left:85px">
    <div class="thumb" role="img" aria-label="Business team meeting around a conference table"></div>
    <div class="date">2 APRIL 2023</div>
    <h5>Lorem ipsum dolor sit amet</h5>
    <p>Lorem ipsum dolor sit amet consect etur adipiscing elit sdsg</p>
    <a class="btn-blue" href="#">Read More</a>
  </article>
  <article class="card abs" style="left:442px">
    <div class="thumb" role="img" aria-label="Business team meeting around a conference table"></div>
    <div class="date">2 APRIL 2023</div>
    <h5>Lorem ipsum dolor sit amet</h5>
    <p>Lorem ipsum dolor sit amet consect etur adipiscing elit sdsg</p>
    <a class="btn-blue" href="#">Read More</a>
  </article>
  <article class="card abs" style="left:801px">
    <div class="thumb" role="img" aria-label="Business team meeting around a conference table"></div>
    <div class="date">2 APRIL 2023</div>
    <h5>Lorem ipsum dolor sit amet</h5>
    <p>Lorem ipsum dolor sit amet consect etur adipiscing elit sdsg</p>
    <a class="btn-blue" href="#">Read More</a>
  </article>
</section>

<section class="contact abs">
  <h2 class="sec-title abs">CONTACT US<span class="mark"><i class="g"></i><i class="o"></i><i class="b"></i></span></h2>
  <div class="field abs" style="left:223px;top:216px;width:387px;height:72px">First Name*</div>
  <div class="field abs" style="left:222px;top:302px;width:385px;height:73px">Phone Number*</div>
  <div class="field abs" style="left:222px;top:393px;width:385px;height:72px">Email Address*</div>
  <div class="field msg abs" style="left:638px;top:216px;width:414px;height:159px">Message*</div>
  <a class="btn-blue abs" href="#">Submit</a>
</section>

<section class="info abs">
  <div class="info-item abs" style="left:85px">
    <span class="ic" style="background:var(--blue)">
      <svg width="22" height="30" viewBox="0 0 22 30"><path d="M11 0a11 11 0 0 0-11 11c0 8 11 19 11 19s11-11 11-19A11 11 0 0 0 11 0z" fill="#fff"/><circle cx="11" cy="11" r="4" fill="var(--blue)"/></svg>
    </span>
    <span style="margin-left:-2px">Suite 12/40 Harbourline Road,<br>Eastvale WA 6021</span>
  </div>
  <div class="info-item abs" style="left:427px">
    <span class="ic" style="background:var(--orange)">
      <svg width="28" height="28" viewBox="0 0 24 24"><path d="M6.6 10.8a15 15 0 0 0 6.6 6.6l2.2-2.2a1 1 0 0 1 1-.25 11.4 11.4 0 0 0 3.6.57 1 1 0 0 1 1 1V20a1 1 0 0 1-1 1A17 17 0 0 1 3 4a1 1 0 0 1 1-1h3.5a1 1 0 0 1 1 1 11.4 11.4 0 0 0 .57 3.6 1 1 0 0 1-.25 1z" fill="#fff"/></svg>
    </span>
    <span style="margin-left:-10px">+61 (08) 5550 1234 (Sales / Support)</span>
  </div>
  <div class="info-item abs" style="left:801px">
    <span class="ic" style="background:var(--green)">
      <svg width="32" height="22" viewBox="0 0 32 22"><rect x="1" y="1" width="30" height="20" fill="none" stroke="#fff" stroke-width="2"/><path d="M1 1l15 11L31 1M1 21l11-9M31 21l-11-9" fill="none" stroke="#fff" stroke-width="2"/></svg>
    </span>
    <span style="margin-left:-6px">hello@quorvexlabworks.com</span>
  </div>
</section>

<footer class="footer abs">
  <div class="brand abs"><span class="dot"></span>Quorvex Labworks</div>
  <nav class="foot-nav abs">
    <a href="#">Home</a>
    <a href="#">Services</a>
    <a href="#">Products</a>
    <a href="#">Blog</a>
    <a href="#">Contact us</a>
  </nav>
  <div class="rule abs"></div>
  <div class="copy abs">Copyright @&nbsp;&nbsp; 2023 All rights reserved</div>
  <div class="social abs"><span></span><span></span><span></span><span></span></div>
</footer>

</body>
</html>
```